Flyer-Design für  junges, dynamisches Unternehmen, spezialisiert auf innovative Trainingskonzepte
Flyer-Design für junges, dynamisches Unternehmen, spezialisiert auf innovative Trainingskonzepte
dqlVIT
Sehr kreative und ideenreiche Umsetzungen. Alle Wünsche sind sehr sorgfältig, gewissenhaft und mit absoluter Schnelligkeit erfolgt.
Zielgruppe
Als junges dynamisches Unternehmen ist dqlVIT spezialisiert auf innovative Trainingskonzepte. Wir sind
ein international anerkanntes Trainingscenter der Northfield Rescue Alliance und bieten Notfalltrainings,
Erste-Hilfe-Kurse sowie hochwertige Simulationstrainings fur Rettungsdienste und Krankenhäuser an. In
unseren CRM- Simulationstrainings coachen wir Notfallteams in den Bereichen Skills, Human Factor und
Kommunikation. Hierbei kommen Full-Scale-Simulatoren und Schauspielpatienten zum Einsatz, die eine
realitätsnahe und lebensechte Trainingssituation präsentieren.
Aufgabenstellung
Wir suchen zur Vermarktung unserer Kurse eine graphische Übersicht, aus der die Qualitätsmerkmale von dqlVIT, eine Zielgruppen definition sowie eine detailierte Aufarbeitung der Kursinhalte in den Verschiedenen Kursformaten hervorgeht und unsere zukünftigen Kunden von uns überzeugt.
Großer Fokus dieses Projektes, ist es die Innenseite des Flyers zu gestalten, die ein geschlossenes Gesamtbild aufweisen soll. Deckblatt und Rückseite sind nebensächlich, hier freuen wir uns über neue Ideen, aber das Fokus ist die Gestaltung der Innenseite.

```html
<!DOCTYPE html>
<html lang="de">
<head>
<meta charset="utf-8">
<title>dqlVIT – Kursdetails &amp; Preise</title>
<link href="https://fonts.googleapis.com/css2?family=PT+Sans+Narrow:wght@400;700&family=Source+Sans+3:ital,wght@0,400;0,600;1,400;1,600;1,700&family=Open+Sans:ital,wght@1,800&display=swap" rel="stylesheet">
<style>
:root{
  --red:#d9191f;
  --red-dark:#a50f18;
  --grey-band:#4a4a4a;
  --line:#5a5a5a;
  --text:#333;
  --panel:#e4e4e6;
  --white:#fff;
}
*{margin:0;padding:0;box-sizing:border-box}
html,body{width:1200px;height:849px;overflow:hidden;background:var(--white)}
.flyer{position:relative;width:1200px;height:849px;overflow:hidden;font-family:"Source Sans 3",sans-serif;color:var(--text)}
.top-band{position:absolute;left:0;top:0;width:1200px;height:90px}
.page-title{position:absolute;left:145px;top:12px;font-family:"Open Sans",sans-serif;font-style:italic;font-weight:800;font-size:27px;color:var(--white);letter-spacing:.3px}
.connectors{position:absolute;left:0;top:0}
.tier-head{position:absolute;width:186px;height:42px;display:flex;align-items:center;justify-content:center;font-family:"PT Sans Narrow",sans-serif;font-weight:700;font-size:19px;color:var(--white);text-shadow:0 1px 2px rgba(0,0,0,.45);box-shadow:2px 3px 5px rgba(0,0,0,.25)}
.tier-light{background:linear-gradient(#e8b764 0,#efc56e 48%,#fbe08a 52%,#fcec9f 100%)}
.tier-basic{background:linear-gradient(#d2800c 0,#df920f 48%,#f19a5e 52%,#f6b489 100%)}
.tier-premium{background:linear-gradient(#9c9c9c 0,#b0b0b0 48%,#d4d4d4 52%,#e6e6e6 100%)}
.tier-plus{background:linear-gradient(#eea012 0,#f2b00f 48%,#ffd800 52%,#ffea00 100%)}
.tier-price{position:absolute;top:159px;font-family:"PT Sans Narrow",sans-serif;font-weight:700;font-size:10.5px;color:#3a3a3a;white-space:nowrap}
.item{position:absolute;width:186px;height:45px;background:var(--white);border:1.3px solid var(--red);box-shadow:2px 3px 5px rgba(0,0,0,.22);padding:0 10px 0 12px;display:flex;align-items:center;font-family:"PT Sans Narrow",sans-serif;font-size:9px;line-height:1.33;color:#333}
.item.tall{height:109px}
.footnote{position:absolute;left:393px;top:551px;font-style:italic;font-size:14px;color:#444}
.benefits-title{position:absolute;left:870px;top:446px;font-style:italic;font-weight:700;font-size:11.5px;color:var(--red)}
.benefits{position:absolute;left:870px;top:472px;list-style:none;font-size:9.6px;line-height:15.2px;color:#444}
.benefits li::before{content:"-  ";}
.info-panel{position:absolute;left:0;top:621px;width:1200px;height:228px;background:var(--panel)}
.course-text{position:absolute;left:36px;width:506px;font-size:9.8px;line-height:13.2px;color:#444}
.course-text b{font-style:italic;font-weight:700;font-size:12px;color:var(--red)}
.photo{position:absolute;top:621px;height:170px}
.bottom-band{position:absolute;left:0;top:0}
.site-url{position:absolute;left:1006px;top:814px;font-family:"Open Sans",sans-serif;font-style:italic;font-weight:800;font-size:18px;color:var(--white);letter-spacing:.3px}
</style>
</head>
<body>
<main class="flyer">
  <svg class="top-band" viewBox="0 0 1200 90" aria-hidden="true">
    <defs>
      <linearGradient id="bandRed" x1="0" x2="1">
        <stop offset="0" stop-color="#a50f18"/><stop offset=".5" stop-color="#d41a20"/><stop offset="1" stop-color="#e3232a"/>
      </linearGradient>
    </defs>
    <path d="M0 0H1160C1050 35 700 60 0 62Z" fill="url(#bandRed)"/>
    <path d="M0 62C500 66 700 58 780 52C700 62 400 80 0 80Z" fill="#4a4a4a"/>
  </svg>
  <h1 class="page-title">Kursdetails &amp; Preise</h1>

  <svg class="connectors" width="1200" height="849" aria-hidden="true" fill="none" stroke="#5a5a5a" stroke-width="1">
    <path d="M130 125H117V521H130M117 205H130M117 269H130M117 331H130M117 394H130M117 458H130"/>
    <path d="M238 227V245M238 290V308M238 353V372M238 417V435M238 480V499M238 544V589"/>
    <path d="M380 125H360V564H238M360 205H372M360 269H372M360 331H372M360 394H372M360 458H372"/>
    <path d="M478 227V245M478 290V308M478 353V372M478 417V435M478 480V589"/>
    <path d="M621 125H600V577H238M600 205H613M600 269H613M600 363H613"/>
    <path d="M722 227V245M722 290V308M722 417V589"/>
    <path d="M863 125H843V589H238M843 205H855M843 269H855M843 363H855"/>
  </svg>

  <div class="tier-head tier-light" style="left:145px;top:103px">Light</div>
  <div class="tier-head tier-basic" style="left:387px;top:103px">Basic*</div>
  <div class="tier-head tier-premium" style="left:629px;top:103px">Premium*</div>
  <div class="tier-head tier-plus" style="left:872px;top:103px">PremiumPLUS*</div>

  <p class="tier-price" style="left:145px">2Std. | BLS | 1 Instruktor: 123,- €</p>
  <p class="tier-price" style="left:387px">3 Std. | 1 Instruktor | BLS + CRM: 234,- €</p>
  <p class="tier-price" style="left:629px">4 Std. | 1 Instruktor | BLS+CRM: 456,- €</p>
  <p class="tier-price" style="left:872px">Ab 4 Std. | 2 Intruktoren | BLS+ALS+CRM: 7890,- €</p>

  <div class="item" style="left:145px;top:182px">Vorstellungen und Erläuterung des<br>Basic-Life-Support für med. Fachpersonal</div>
  <div class="item" style="left:145px;top:245px">Auffinden eines bewusstlosen Patienten</div>
  <div class="item" style="left:145px;top:308px">High-Performance-Reanimation, 5 Kriterien für<br>eine perfekte Herz-Druck-Massage</div>
  <div class="item" style="left:145px;top:372px">Vorstellung Beutel-Masken-Beatmung, LTTubus<br>und Pocketmaske</div>
  <div class="item" style="left:145px;top:435px">Vorstellung und Anwendung AED (Defi)</div>
  <div class="item" style="left:145px;top:499px">Trainingsszenarien zum Ablauf einer Reanimation</div>

  <div class="item" style="left:387px;top:182px">Übungen zur Beatmung für jeden Teilnehmer</div>
  <div class="item" style="left:387px;top:245px">Übungen mit dem AED für jeden Teilnehmer</div>
  <div class="item" style="left:387px;top:308px">Elektronische Auswertung der<br>Reanimationsergebnisse</div>
  <div class="item" style="left:387px;top:372px">Training zur Teamkoordination und<br>Teamkommunikation</div>
  <div class="item" style="left:387px;top:435px">Fallbeispiele zur Reanimation mit Feedback zur<br>Aufgabenbewältigung und Kommunikation</div>

  <div class="item" style="left:629px;top:182px">Überprüfung und auf Wunsch Anpassung der<br>internen Abläufe der Rettungskette (QMNotfallplan)</div>
  <div class="item" style="left:629px;top:245px">Fallbeispieltraining mit echtem Patienten<br>(Schauspieler)</div>
  <div class="item tall" style="left:629px;top:308px">Fallbeispiel zu ausgewählten und passenden<br>Themen wie Asthma, Anaphylaxie,<br>Krampfanfall, Bolusgeschehen, Herzinfarkt,<br>etc. die Auswahl erfolgt Anhand der<br>Fachrichtung/Praxisschwerpunkt</div>

  <div class="item" style="left:872px;top:182px">ABCDE-Schema zur Ersteinschätzung von<br>kritisch kranken Patienten</div>
  <div class="item" style="left:872px;top:245px">FORDEC-Training zur Entscheidungsfindung</div>
  <div class="item tall" style="left:872px;top:308px">Fallbeispiele zu lebensbedrohlichen<br>Situationen mit einem High-Tech-Simulator<br>u.a. mit Sprachfunktion, realistischen<br>Atembewegungen mit Atemgeräuschen,<br>Zyanose, tastebaren Pulsen und der<br>Durchführung von Maßnahmen (z.B.:<br>Entlastungspunktion, Infusiontherapie, etc.)</div>

  <p class="footnote">*Beinhaltet immer die vorrausgehenden Kurspackete</p>

  <h2 class="benefits-title">Was sind unsere Vorteile/Was zeichnet dqlVIT aus?</h2>
  <ul class="benefits">
    <li>Zertifizierte und anerkannte Kurskonzepte</li>
    <li>Angenehme Lernatmosphäre mit emphatischen Instruktoren</li>
    <li>Realistische Aus- und Fortbildung mit Schauspielpatienten</li>
    <li>Modernstes Material, Technik und Simulatoren</li>
    <li>Alle Dozenten mit langjähriger Erfahrung in der Notfallmedizin</li>
    <li>Praxisorientierte und individuelle Kursgestaltung</li>
    <li>Durchführung der Schulungen bei unseren Kunden Inhouse vor Ort</li>
    <li>Förderung der Teamarbeit durch Crew Ressource Management</li>
  </ul>

  <section class="info-panel"></section>
  <p class="course-text" style="top:641px"><b>Notfalltraining Light - </b>Lernen Sie in diesem Skilltraining die Reanimation und beherrschen Sie die Herzdruckmassage. Außerdem besprechen wir die Intubation und die Defibrillation mit einem AED.</p>
  <p class="course-text" style="top:680px"><b>Notfalltraining Basic - </b>Interaktives Team-Training: Üben Sie die wichtigsten Handgriffe und lernen Sie Ihre eigene Notfallausrüstung kennen. Das medizinische Know-How wird durch zusätzliche Themen wie Teamwork und Kommunikation erweitert.</p>
  <p class="course-text" style="top:733px"><b>Notfalltraining Premium - </b>Weg mit der Puppe! Wir bringen unseren Schauspielpatienten mit zu Ihnen! Wir trainieren dynamische Notfälle und gemeinsam mit Ihnen analysieren und optimieren wir Ihr Notfallmanagement in Ihrer Praxis. Mit diesem Training schaffen Sie eine hohe Zufriedenheit mit Ihren Mitarbeitern und sind perfekt auf den nächsten Notfall vorbereitet. Auf Wunsch bieten wir Ihnen eine kostenlose Beratung und Verwaltung Ihrer Notfallausrüstung an.</p>

  <div class="photo" role="img" aria-label="Foto: Herzdruckmassage an einer Reanimationspuppe mit Monitor im Hintergrund" style="left:599px;width:201px;background:linear-gradient(135deg,#3b3f4a,#7a6a62 55%,#c9b9a8)"></div>
  <div class="photo" role="img" aria-label="Foto: Rettungsteam versorgt einen Simulationspatienten am Boden" style="left:803px;width:200px;background:linear-gradient(160deg,#5a5350,#8a7468 50%,#b5493c)"></div>
  <div class="photo" role="img" aria-label="Foto: Notfallsanitäter beatmen einen Patienten mit Beutel-Masken-Beatmung" style="left:1007px;width:193px;background:linear-gradient(150deg,#4a4040,#a5423a 55%,#d7cfc8)"></div>

  <svg class="bottom-band" width="1200" height="849" aria-hidden="true">
    <defs>
      <linearGradient id="footRed" x1="0" x2="1">
        <stop offset="0" stop-color="#b0121a"/><stop offset="1" stop-color="#e3232a"/>
      </linearGradient>
    </defs>
    <path d="M280 817C600 800 900 790 1200 788V800C900 802 600 812 280 817Z" fill="#4a4a4a"/>
    <path d="M40 849C300 815 800 800 1200 798V849Z" fill="url(#footRed)"/>
  </svg>
  <p class="site-url">www.dqlvit.de</p>
</main>
</body>
</html>
```